Business Cards for an 'affordable luxury' inner city home builder in Calgary.

We need a business card design that emulates the progressive, innovative, culture of our company and the modern style of our homes. Use our website www.velmarcrest-ab.com as a reference for the product we build.

Our company builds homes in the inner city space of Calgary, Alberta. We build affordable luxury.

Target Market(s)

Young professional Families

Contact Information for Business Card

Try to maintain consistency with the logo font and the card font.

Requirements
Must have
• The details must include: Name, education, title, phone number, website and email (Address is not as important)
• The design must be uniques (like our logo), elegant, sophisticated and modern.

```html
<!DOCTYPE html>
<html lang="en">
<head>
<meta charset="utf-8">
<title>Velmar Crest Homes Ltd — Business Card</title>
<link rel="stylesheet" href="https://fonts.googleapis.com/css2?family=Montserrat:wght@300;400;500;800&family=Open+Sans:wght@400;600&display=swap">
<style>
  :root {
    --page: #e9e7e4;
    --card-light: #ffffff;
    --card-dark: #3c3c3c;
    --ink: #111111;
    --ink-soft: #2a2a2a;
    --on-dark: #ffffff;
    --url-on-dark: #161616;
    --shadow: rgba(0, 0, 0, 0.18);
  }
  * { box-sizing: border-box; margin: 0; padding: 0; }
  html, body { width: 1200px; height: 900px; overflow: hidden; }
  body {
    background: var(--page);
    display: flex;
    flex-direction: column;
    align-items: center;
    justify-content: center;
    gap: 60px;
    font-family: "Open Sans", sans-serif;
  }
  .card {
    width: 560px;
    height: 320px;
    position: relative;
    box-shadow: 0 10px 28px var(--shadow);
  }

  /* Front */
  .card--front { background: var(--card-light); color: var(--ink); }
  .front-brand {
    position: absolute;
    left: 40px;
    top: 150px;
    display: flex;
    align-items: center;
    gap: 14px;
  }
  .brand-square {
    width: 40px; height: 40px;
    flex: none;
    border: 2px solid var(--ink);
  }
  .brand-name {
    font-family: "Montserrat", sans-serif;
    font-weight: 500;
    font-size: 19px;
    line-height: 1.05;
    letter-spacing: 1px;
    text-transform: uppercase;
    color: var(--ink);
    white-space: nowrap;
  }
  .divider {
    position: absolute;
    left: 276px;
    top: 60px;
    width: 2px;
    height: 210px;
    background: var(--ink);
  }
  .contact {
    position: absolute;
    left: 306px;
    top: 58px;
    width: 236px;
  }
  .person-name {
    font-family: "Montserrat", sans-serif;
    font-size: 24px;
    line-height: 1;
    text-transform: uppercase;
  }
  .person-name .first { font-weight: 800; }
  .person-name .last { font-weight: 300; }
  .person-title {
    font-family: "Montserrat", sans-serif;
    font-weight: 800;
    font-size: 10px;
    letter-spacing: 0.4px;
    margin-top: 3px;
    margin-left: 4px;
    text-transform: uppercase;
  }
  .contact-list { list-style: none; margin-top: 16px; }
  .contact-item {
    display: flex;
    align-items: center;
    gap: 16px;
    font-size: 10.5px;
    color: var(--ink-soft);
    height: 38px;
  }
  .contact-icon { width: 22px; height: 22px; flex: none; }
  .contact-text { line-height: 1.35; white-space: nowrap; }

  /* Back */
  .card--back { background: var(--card-dark); }
  .back-brand {
    position: absolute;
    left: 0; right: 0;
    top: 112px;
    display: flex;
    justify-content: center;
    align-items: center;
    gap: 20px;
  }
  .back-brand .brand-square { width: 54px; height: 54px; border-color: var(--on-dark); }
  .back-brand .brand-name { color: var(--on-dark); font-size: 29px; letter-spacing: 1.5px; }
  .back-url {
    position: absolute;
    left: 150px;
    bottom: 38px;
    font-size: 13px;
    letter-spacing: 0.5px;
    color: var(--url-on-dark);
    text-transform: uppercase;
  }
</style>
</head>
<body>
  <section class="card card--front" aria-label="Business card front">
    <div class="front-brand">
      <span class="brand-square" aria-hidden="true"></span>
      <p class="brand-name">Velmar Crest<br>Homes Ltd</p>
    </div>
    <span class="divider" aria-hidden="true"></span>
    <div class="contact">
      <p class="person-name"><span class="first">Name</span> <span class="last">Here</span></p>
      <p class="person-title">Designation</p>
      <ul class="contact-list">
        <li class="contact-item">
          <svg class="contact-icon" viewBox="0 0 24 24" aria-hidden="true">
            <circle cx="12" cy="12" r="10.5" fill="none" stroke="#111" stroke-width="1.8"/>
            <path d="M8.6 7.2l1.6-.5 1.1 2.4-1 .9c.5 1.2 1.4 2.2 2.7 2.8l.9-1 2.4 1.1-.5 1.6c-.2.6-.8.9-1.4.8-3.3-.6-5.8-3.1-6.4-6.4-.1-.6.2-1.2.6-1.7z" fill="#111"/>
          </svg>
          <span class="contact-text">000 000 0000<br>000 000 0000</span>
        </li>
        <li class="contact-item">
          <svg class="contact-icon" viewBox="0 0 24 24" aria-hidden="true">
            <rect x="2" y="5" width="20" height="14" fill="#111"/>
            <path d="M4.5 7.5L12 13l7.5-5.5V17h-2.5v-6L12 15l-5-4v6H4.5z" fill="#fff"/>
          </svg>
          <span class="contact-text">velmarcrest@example.com</span>
        </li>
        <li class="contact-item">
          <svg class="contact-icon" viewBox="0 0 24 24" aria-hidden="true" fill="none" stroke="#111" stroke-width="1.8">
            <circle cx="12" cy="12" r="10"/>
            <ellipse cx="12" cy="12" rx="4.2" ry="10"/>
            <path d="M2 12h20M4 6.5h16M4 17.5h16"/>
          </svg>
          <span class="contact-text">www.velmarcrest-ab.com</span>
        </li>
      </ul>
    </div>
  </section>

  <section class="card card--back" aria-label="Business card back">
    <div class="back-brand">
      <span class="brand-square" aria-hidden="true"></span>
      <p class="brand-name">Velmar Crest<br>Homes Ltd</p>
    </div>
    <p class="back-url">www.velmarcrest-ab.com</p>
  </section>
</body>
</html>
```